Custom Manufacturing Job Shop

We are looking for a business card design for Tall Oak Fabrication Inc. Tall Oak is a family owned business that manufactures any custom product to fit a customers needs, whether it is custom 1 piece or production parts, we truly take on projects that others just cant do. to help in your design go to www.talloakfab.example for a more in depth idea. we have the following capabilities that we would like to see on the card somewhere...maybe on the back of a 2 sided card? we are fully open to ideas.
Machining
• Fabrication
• Millwork
• Maintenance
• Laser Cutting
• Precision Forming
Engineering
Blasting/Painting

No matter how big or small, We literally do it all

preferably black or darker cards but we don't mind to see some color if you see a better fit. we are interested in looking at anything that catches attention.
I have attached our logo, if it is needed in a different file type please let me know and I will send it to you if I can. maybe adding some type of drawing or dimensional lines would be something to add?? just throwing ideas out there....

Reason: I added one of our shredder designs and would like to see a few more cards if possible using this. any questions please don't hesitate to ask!!

Target Market(s)

anyone looking for design/manufacturing/machining whether it is custom 1 off parts or production.

Industry/Entity Type

Business

Contact Information for Business Card

preferably darker shades, but also not opposed to some color in the same sense....not too bright

Font styles to use
Serif
Sans Serif

Requirements
Must have
• Dell Marwick
• Direct:555-213-7790
• Cell:555-348-1162
• Fax: 555-907-4425
• 42 Quarry Lane
• Klingerstown, PA 00000
• I also would request having it in a format I can give to the company making the business cards to edit names/numbers etc. for the entire staff.
Nice to have
• drafting lines? we are open to almost anything....
Should not have
• exotic colors

```html
<!DOCTYPE html>
<html lang="en">
<head>
<meta charset="utf-8">
<title>Tall Oak Fabrication – Business Card</title>
<link rel="stylesheet" href="https://fonts.googleapis.com/css2?family=Exo+2:wght@400;500;700&display=swap">
<style>
  :root {
    --page-bg: #d9d9d9;
    --card-bg: #f4f4f4;
    --ink: #2a2a2a;
    --ink-soft: #505050;
    --band-light: #bcbcbc;
    --band-dark: #666666;
    --logo-grey: #474747;
    --logo-sub: #999999;
  }
  * { box-sizing: border-box; margin: 0; padding: 0; }
  html, body {
    width: 1200px; height: 900px; overflow: hidden;
    background: var(--page-bg);
    font-family: "Exo 2", sans-serif;
  }
  .card {
    position: absolute; left: 100px; top: 165px;
    width: 1000px; height: 570px;
    background: linear-gradient(160deg, #ffffff 0%, var(--card-bg) 60%, #e9e9e9 100%);
    border-radius: 46px; overflow: hidden;
    box-shadow: 0 12px 30px rgba(0,0,0,.18);
  }
  .card__waves { position: absolute; inset: 0; width: 100%; height: 100%; }
  .brand { position: absolute; left: 70px; top: 232px; }
  .brand__name {
    display: flex; align-items: center; gap: 14px;
    font-weight: 700; font-size: 58px; letter-spacing: 2px;
    color: var(--logo-grey); line-height: 1;
  }
  .brand__mark { width: 40px; height: 40px; border-radius: 50%; background: var(--logo-grey); }
  .brand__web {
    margin-top: 10px; margin-left: 58px;
    font-size: 18px; letter-spacing: 2px; color: var(--logo-sub);
  }
  .contact {
    position: absolute; right: 70px; top: 42px;
    text-align: right; color: var(--ink);
  }
  .contact__name { font-size: 30px; font-weight: 500; letter-spacing: 1.5px; line-height: 1.15; }
  .contact__title { font-size: 20px; color: var(--ink-soft); margin-top: 2px; }
  .contact__address { font-size: 20px; margin-top: 26px; line-height: 1.3; letter-spacing: .5px; }
  .contact__list { list-style: none; margin-top: 20px; font-size: 16px; line-height: 1.85; letter-spacing: .8px; }
  .contact__list li { display: flex; justify-content: flex-end; align-items: center; gap: 10px; }
  .contact__list svg { width: 16px; height: 16px; fill: var(--ink); flex: none; }
</style>
</head>
<body>
  <section class="card" aria-label="Business card front">
    <svg class="card__waves" viewBox="0 0 1000 570" preserveAspectRatio="none" aria-hidden="true">
      <path fill="var(--band-light)" d="M0,440 C280,490 540,460 740,395 C870,352 950,342 1000,340 L1000,570 L0,570 Z"/>
      <path fill="var(--band-dark)" d="M0,560 C260,575 520,548 740,465 C870,415 950,395 1000,390 L1000,570 L0,570 Z"/>
      <path fill="none" stroke="#ffffff" stroke-width="5" d="M0,553 C260,568 520,541 740,458 C870,408 950,388 1000,383"/>
    </svg>

    <div class="brand">
      <div class="brand__name"><span class="brand__mark"></span>TALL OAK</div>
      <div class="brand__web">TALLOAKFAB.EXAMPLE</div>
    </div>

    <div class="contact">
      <p class="contact__name">DELL MARWICK</p>
      <p class="contact__title">Managing Director</p>
      <p class="contact__address">42 Quarry Lane<br>Klingerstown, PA 00000</p>
      <ul class="contact__list">
        <li>555-213-7790
          <svg viewBox="0 0 24 24"><path d="M6.6 10.8a15 15 0 0 0 6.6 6.6l2.2-2.2c.3-.3.7-.4 1-.2 1.1.4 2.3.6 3.6.6.6 0 1 .4 1 1V20c0 .6-.4 1-1 1A17 17 0 0 1 3 4c0-.6.4-1 1-1h3.5c.6 0 1 .4 1 1 0 1.3.2 2.5.6 3.6.1.3 0 .7-.2 1z"/></svg></li>
        <li>555-348-1162
          <svg viewBox="0 0 24 24"><path d="M7 1h10a2 2 0 0 1 2 2v18a2 2 0 0 1-2 2H7a2 2 0 0 1-2-2V3a2 2 0 0 1 2-2zm0 3v14h10V4zm5 15.5a1 1 0 1 0 0 2 1 1 0 0 0 0-2z"/></svg></li>
        <li>555-907-4425
          <svg viewBox="0 0 24 24"><path d="M6 2h9v5H6zM4 8h16a2 2 0 0 1 2 2v9a2 2 0 0 1-2 2H4a2 2 0 0 1-2-2v-9a2 2 0 0 1 2-2zm2 4v2h4v-2zm0 4v2h4v-2zm8-4v6h4v-6z"/></svg></li>
        <li>dell@talloakfab.example
          <svg viewBox="0 0 24 24"><path d="M2 5h20v14H2zm2 2v.5l8 5 8-5V7zm0 3v7h16v-7l-8 5z"/></svg></li>
        <li>www.talloakfab.example
          <svg viewBox="0 0 24 24"><path d="M12 2a10 10 0 1 0 0 20 10 10 0 0 0 0-20zm6.9 6h-3a15 15 0 0 0-1.3-3.9A8 8 0 0 1 18.9 8zM12 4c.8 1.2 1.5 2.5 1.9 4h-3.8c.4-1.5 1.1-2.8 1.9-4zM4.3 14a8 8 0 0 1 0-4h3.4a16 16 0 0 0 0 4zm.8 2h3a15 15 0 0 0 1.3 3.9A8 8 0 0 1 5.1 16zm3-8h-3a8 8 0 0 1 4.3-3.9A15 15 0 0 0 8.1 8zM12 20c-.8-1.2-1.5-2.5-1.9-4h3.8c-.4 1.5-1.1 2.8-1.9 4zm2.3-6H9.7a14 14 0 0 1 0-4h4.6a14 14 0 0 1 0 4zm.3 5.9a15 15 0 0 0 1.3-3.9h3a8 8 0 0 1-4.3 3.9zm1.7-5.9a16 16 0 0 0 0-4h3.4a8 8 0 0 1 0 4z"/></svg></li>
      </ul>
    </div>
  </section>
</body>
</html>
```